Truck Drivers Using App w/Jobsite Checklist

Looking for an 8" x 11" flyer that conveys to our customers (roofing contractors) that our drivers have tablets in each truck that have an app with a jobsite checklist that gives contractors less real time notifications and mistakes are caught with photos.
Should read something like this:
Ever wonder if your material has been delivered? We've got a solution for that!
All Trucks are equipped with dash-mounted tablet.
Here's what you get access to:
- Real Time Email Confirmation of Delivery
- Photos of Material Placement
- Before/After Photo of Driveway
- Material List of Products Delivered
- Homeowner Sign Off
Maybe a collage of the different photos available.
Target Market(s)
Roofing/Building Contractors
Industry/Entity Type
Roofing
Requirements
Must have
- website: www.harborfinchbuild.com
- tagline: Building Relationships, Building Trust - a Tradition Since 1905
- Photoshop format for further editing
Nice to have
- A smooth look to it.
- A collage of the photos avail on app

```html
<!DOCTYPE html>
<html lang="en">
<head>
<meta charset="utf-8">
<title>Harbor Finch Supply – Delivery Checklist Flyer</title>
<link href="https://fonts.googleapis.com/css2?family=Oswald:wght@400;500;600&display=swap" rel="stylesheet">
<style>
  :root {
    --navy: #2e3192;
    --navy-deep: #262a7e;
    --navy-light: #3b3f9e;
    --gold: #c8a45a;
    --white: #ffffff;
    --check: #e6e2ee;
    --stage: #e9e6e1;
  }
  * { box-sizing: border-box; margin: 0; padding: 0; }
  html, body {
    width: 969px; height: 1200px; overflow: hidden;
    background: var(--stage);
    font-family: "Oswald", "Arial Narrow", sans-serif;
  }
  .sheet-holder {
    position: absolute; left: 70px; top: 30px;
    width: 828px; height: 1140px;
  }
  .flyer {
    position: absolute; left: 0; top: 0;
    width: 695px; height: 957px;
    transform: scale(1.1913); transform-origin: 0 0;
    background: radial-gradient(ellipse at 55% 45%, var(--navy-light) 0%, var(--navy) 55%, var(--navy-deep) 100%);
    overflow: hidden;
  }
  .header-wave { position: absolute; left: 0; top: 0; width: 695px; height: 220px; }

  .brand {
    position: absolute; left: 20px; top: 38px; width: 190px; text-align: center;
  }
  .brand-dot {
    display: block; width: 38px; height: 38px; border-radius: 50%;
    background: var(--navy); margin: 0 auto 10px;
  }
  .brand-name {
    font-size: 18px; font-weight: 600; color: var(--navy);
    letter-spacing: 1px; line-height: 1.1; white-space: nowrap;
  }
  .tagline {
    position: absolute; left: 15px; top: 134px; width: 200px;
    text-align: center; font-size: 13px; line-height: 1.15; color: var(--navy);
  }

  .headline { position: absolute; left: 222px; top: 58px; text-transform: uppercase; white-space: nowrap; }
  .headline-question { font-size: 18.8px; font-weight: 600; color: var(--navy); line-height: 1.2; }
  .headline-answer { font-size: 30px; font-weight: 600; color: var(--gold); line-height: 1.2; }

  .hand-photo {
    position: absolute; left: 48px; top: 315px; width: 185px; height: 300px;
    background: radial-gradient(ellipse at 50% 55%, rgba(226,176,140,.55) 0%, rgba(226,176,140,.25) 55%, rgba(226,176,140,0) 80%);
  }
  .check-icon { position: absolute; left: 140px; top: 240px; width: 80px; height: 78px; opacity: .8; }

  .equipped {
    position: absolute; left: 248px; top: 254px; white-space: nowrap;
    font-size: 19.5px; font-weight: 500; color: var(--gold);
  }
  .access-title {
    position: absolute; left: 309px; top: 313px;
    font-size: 19px; font-weight: 500; color: var(--white);
  }
  .access-list { position: absolute; left: 309px; top: 360px; list-style: none; }
  .access-list li {
    position: relative; height: 34px; padding-left: 55px; white-space: nowrap;
    font-size: 18px; color: var(--white); line-height: 28px;
  }
  .access-list li::before {
    content: ""; position: absolute; left: 0; top: 8px;
    width: 13px; height: 13px; background: var(--gold);
  }

  .collage {
    position: absolute; left: 0; top: 615px; width: 695px; height: 300px;
    background: var(--white);
  }
  .collage-photo { position: absolute; }
  .photo-driver   { left: 0;     top: 8px;   width: 231px; height: 158px; background: linear-gradient(120deg, #e4e4e1 0%, #d6d3c6 45%, #c9cf7a 70%, #7f90a6 100%); }
  .photo-truck    { left: 240px; top: 8px;   width: 205px; height: 158px; background: linear-gradient(180deg, #6aa6df 0%, #cfe2f2 35%, #eef0f1 55%, #8b8e92 80%, #3d3f43 100%); }
  .photo-dash     { left: 460px; top: 8px;   width: 235px; height: 158px; background: linear-gradient(180deg, #e6e8e8 0%, #c4c8c9 45%, #6d7174 70%, #262729 100%); }
  .photo-load     { left: 0;     top: 175px; width: 264px; height: 117px; background: linear-gradient(180deg, #a7bdd9 0%, #ece7e5 40%, #d9cfcf 60%, #3b3c40 100%); }
  .photo-roof     { left: 274px; top: 175px; width: 261px; height: 117px; background: linear-gradient(180deg, #d3d6d8 0%, #e3e5e6 40%, #55575d 70%, #2c2d33 100%); }
  .photo-driveway { left: 545px; top: 175px; width: 150px; height: 117px; background: linear-gradient(180deg, #3a3a3b 0%, #5c5d5f 60%, #717274 100%); }

  .site-band {
    position: absolute; left: 0; top: 915px; width: 695px; height: 42px;
    background: var(--navy); color: var(--white);
    font-size: 19px; font-weight: 500; text-align: center; line-height: 42px;
  }
</style>
</head>
<body>
<div class="sheet-holder">
  <article class="flyer">
    <svg class="header-wave" viewBox="0 0 695 220" aria-hidden="true">
      <path d="M0 0 H695 V152 C420 165 160 210 0 205 Z" fill="#c8a45a"/>
      <path d="M0 0 H695 V140 C430 150 170 200 0 158 Z" fill="#ffffff"/>
    </svg>

    <div class="brand">
      <span class="brand-dot"></span>
      <div class="brand-name">HARBOR FINCH SUPPLY</div>
    </div>
    <p class="tagline">Building Relationships, Building Trust<br>a Tradition Since 1905</p>

    <div class="headline">
      <p class="headline-question">Ever wonder if your material has been delivered?</p>
      <p class="headline-answer">We've got a solution for that!</p>
    </div>

    <div class="hand-photo" role="img" aria-label="Photo of a hand with the index finger raised toward the checkbox"></div>
    <svg class="check-icon" viewBox="0 0 80 78" aria-hidden="true">
      <path d="M5 12 H52 V22 H15 V66 H60 V40 H70 V76 H5 Z" fill="#e6e2ee"/>
      <path d="M24 34 L38 50 L70 4 L80 10 L39 66 L17 40 Z" fill="#e6e2ee"/>
    </svg>

    <p class="equipped">All Trucks are equipped with dash-mounted tablet.</p>
    <p class="access-title">Here's what you get access to:</p>
    <ul class="access-list">
      <li>Real Time Email Confirmation of</li>
      <li>Delivery</li>
      <li>Photos of Material Placement</li>
      <li>Before/After Photo of Driveway</li>
      <li>Material List of Products Delivered</li>
      <li>Homeowner Sign Off</li>
    </ul>

    <section class="collage">
      <div class="collage-photo photo-driver" role="img" aria-label="Photo of a delivery driver in a safety vest holding a tablet"></div>
      <div class="collage-photo photo-truck" role="img" aria-label="Photo of a flatbed delivery truck with a boom crane under a blue sky"></div>
      <div class="collage-photo photo-dash" role="img" aria-label="Photo of a dash-mounted tablet inside a truck cab on the highway"></div>
      <div class="collage-photo photo-load" role="img" aria-label="Photo of roofing material bundles strapped on a truck bed"></div>
      <div class="collage-photo photo-roof" role="img" aria-label="Photo of roofing bundles placed on a roof deck"></div>
      <div class="collage-photo photo-driveway" role="img" aria-label="Photo of a clean driveway after delivery"></div>
    </section>

    <footer class="site-band">www.harborfinchbuild.com</footer>
  </article>
</div>
</body>
</html>
```